Upmarket Bathroom and Kitchen ware supplier needs a classy business card design

We are a company based in Fiji, we sell plumbing ware (Kitchen and bathroom taps, Basins,showers, toilets etc) through up market show rooms to individuals and directly through Architects and designers of resorts and holiday houses for new builds and renovations. we are wanting to upgrade our over all look and brand. we are starting with a new logo but will be rebranding the whole business. This project is for a business card design for my management and tales team I would like it to be dark, classy and interesting

Target Market(s)

Resort directors and Management, High end holiday home owners

Contact Information for Business Card

Neil Dawson
Director
+64219473815

Colors

Designer to choose colors to be used in the design.

Requirements
Must have
• Must have an upmarket appearance I like darker charcoal shades but will be guided by the designers
• Please any catch phrases like "Crafting remarkable living rooms" this belongs tpo one of our suppliers so can not be used.
Nice to have
• Double sided, so front dedicated to logo provided and back info about the business and the person.

```html
<!DOCTYPE html>
<html lang="en">
<head>
<meta charset="utf-8">
<title>Lagoon Fixtures – Business Card</title>
<link rel="stylesheet" href="https://fonts.googleapis.com/css2?family=Cinzel:wght@600;700&family=Montserrat:wght@300;400;500&display=swap">
<style>
  :root {
    --backdrop: #2591b6;
    --card-black: #050505;
    --card-paper: #ecebe6;
    --marble-dark: #1a1a1a;
    --marble-light: #e4e3de;
    --ink-light: #d9d9d9;
    --logo-ink: #2b2b2b;
  }
  * { box-sizing: border-box; margin: 0; padding: 0; }
  html, body {
    width: 1200px;
    height: 900px;
    overflow: hidden;
    background: var(--backdrop);
  }
  .sheet {
    position: relative;
    width: 1200px;
    height: 900px;
  }
  .card {
    position: absolute;
    left: 250px;
    width: 700px;
    height: 400px;
    overflow: hidden;
    box-shadow: 0 10px 30px rgba(0, 0, 0, 0.25);
  }
  .card--front { top: 40px; background: var(--card-paper); }
  .card--back  { top: 460px; background: var(--card-black); }

  .marble {
    position: absolute;
    top: 0;
    bottom: 0;
    background: linear-gradient(125deg,
      var(--marble-dark) 0%, #6e6e6c 22%, var(--marble-light) 40%,
      #8a8a88 58%, var(--marble-dark) 72%, #b8b7b3 88%, var(--marble-light) 100%);
  }
  .card--front .marble { left: 0; right: 0; }
  .card--back .marble  { left: 0; width: 260px; }

  .brand-panel {
    position: absolute;
    left: 215px;
    top: 60px;
    width: 280px;
    height: 280px;
    background: var(--card-paper);
    display: flex;
    flex-direction: column;
    align-items: center;
    justify-content: center;
    gap: 10px;
  }
  .brand-name {
    font-family: "Montserrat", sans-serif;
    font-weight: 300;
    font-size: 30px;
    letter-spacing: 0.32em;
    color: var(--logo-ink);
    padding-left: 0.32em;
  }
  .brand-rule {
    width: 200px;
    height: 1px;
    background: var(--logo-ink);
  }
  .brand-sub {
    font-family: "Montserrat", sans-serif;
    font-weight: 300;
    font-size: 13px;
    letter-spacing: 0.4em;
    color: var(--logo-ink);
    padding-left: 0.4em;
  }

  .contact {
    position: absolute;
    left: 260px;
    right: 0;
    top: 0;
    bottom: 0;
    padding: 150px 50px 0 40px;
    color: var(--ink-light);
  }
  .contact-name {
    font-family: "Cinzel", serif;
    font-weight: 700;
    font-size: 46px;
    letter-spacing: 0.01em;
    text-align: right;
    line-height: 1;
  }
  .contact-role {
    font-family: "Montserrat", sans-serif;
    font-weight: 400;
    font-size: 17px;
    letter-spacing: 0.14em;
    text-align: right;
    margin-top: 10px;
  }
  .contact-phone {
    font-family: "Montserrat", sans-serif;
    font-weight: 500;
    font-size: 17px;
    letter-spacing: 0.08em;
    margin-top: 12px;
    margin-left: 120px;
  }
</style>
</head>
<body>
  <main class="sheet">
    <section class="card card--front" aria-label="Card front">
      <div class="marble" role="img" aria-label="Black and white swirling marble pattern"></div>
      <div class="brand-panel">
        <span class="brand-name">LAGOON</span>
        <span class="brand-rule"></span>
        <span class="brand-sub">FIXTURES</span>
      </div>
    </section>

    <section class="card card--back" aria-label="Card back">
      <div class="marble" role="img" aria-label="Black and white swirling marble pattern"></div>
      <div class="contact">
        <h1 class="contact-name">NEIL DAWSON</h1>
        <p class="contact-role">DIRECTOR</p>
        <p class="contact-phone">+64219473815</p>
      </div>
    </section>
  </main>
</body>
</html>
```